Lullio.com re-design on Wix platform

Re-do this website : www.lullio.com
Lullio is a sound conditioner that uses the calming, sedative qualities of mundane rhythmic stimulation to allow its users to rest easier and deeper than they normally would.
I think of Lullio.com as a web app; a place to use and buy the product. Im open to suggestion on site layouts, whether you use one page or several.
Use the same color scheme: purple, white, black, grey/silver
I would like a place for testimonials, even though you don't currently see one on the site. Other than that, assume the content will stay mostly the same.
I'd like a clean, modern, professional look. The site will reside on Wix platform.

```html
<!DOCTYPE html>
<html lang="en">
<head>
<meta charset="utf-8">
<title>Lullio — Sleep.Deep.Easy.</title>
<link rel="stylesheet" href="https://fonts.googleapis.com/css2?family=Open+Sans:ital,wght@0,400;0,600;0,700;0,800;1,400&family=Fredoka:wght@500;600&display=swap">
<style>
:root{
  --purple:#8e3fb5;
  --purple-soft:#a66fc4;
  --magenta:#b41fc2;
  --ink:#2b2b2b;
  --grey-text:#6e6e6e;
  --grey-light:#9a9a9a;
  --panel:#f3f3f3;
  --white:#ffffff;
  --night:#191919;
  --night-deep:#121212;
  --field:#222222;
  --field-line:#2f2f2f;
}
*{margin:0;padding:0;box-sizing:border-box}
html,body{width:1200px;height:3579px;overflow:hidden}
body{position:relative;font-family:"Open Sans",Arial,sans-serif;color:var(--ink);background:var(--white)}
.abs{position:absolute}
.heading{font-family:"Fredoka","Open Sans",sans-serif;font-weight:600}

/* hero */
.hero{left:0;top:0;width:1200px;height:800px;
  background:linear-gradient(180deg,#3b3b3d 0%,#4e4e51 35%,#6a6a6d 60%,#b8b8ba 82%,#ffffff 100%)}
.logo{left:75px;top:38px;display:flex;align-items:center;gap:10px;color:var(--white);font-weight:700;font-size:44px;letter-spacing:1px}
.logo .mark{width:14px;height:14px;background:var(--purple)}
.main-nav{left:440px;top:58px;display:flex;gap:28px;font-size:12px;font-weight:600;color:var(--white)}
.main-nav .active{position:relative}
.main-nav .active::after{content:"";position:absolute;left:0;right:0;bottom:-8px;height:2px;background:var(--purple-soft)}
.slide-dots{left:82px;top:287px;display:flex;flex-direction:column;gap:19px}
.slide-dots span{width:12px;height:12px;border:1.5px solid var(--white);border-radius:50%}
.slide-dots .on{background:radial-gradient(circle,var(--white) 35%,transparent 40%)}
.social{left:1080px;top:245px;display:flex;flex-direction:column;gap:49px}
.social span{width:14px;height:14px;border-radius:50%;background:var(--white)}
.social span.first{background:var(--purple-soft)}
.hero-title{left:0;width:1200px;top:312px;text-align:center;color:var(--white);font-weight:700;font-size:46px}
.btn-player{left:465px;top:399px;width:195px;height:63px;border-radius:32px;background:var(--purple);color:var(--white);font-weight:700;font-size:19px;display:flex;align-items:center;justify-content:center;gap:12px}
.scroll-down{left:560px;top:530px}

/* how it works */
.how{left:0;top:871px;width:1200px;height:589px;background:var(--panel)}
.how h2{left:100px;top:100px;color:var(--purple);font-size:28px}
.how .lead{left:100px;top:141px;width:420px;font-size:12px;line-height:21px;font-weight:600;color:var(--grey-text)}
.how ul{left:100px;top:252px;width:390px;list-style:none;font-size:11px;line-height:14px;color:var(--grey-text)}
.how li{position:relative;padding-left:28px;margin-bottom:10px}
.how li::before{content:"";position:absolute;left:2px;top:4px;width:7px;height:7px;border-radius:50%;background:var(--purple)}
.how .close{left:100px;top:436px;width:400px;font-size:12px;line-height:19px;font-weight:600;color:var(--grey-text)}
.sheep-art{left:590px;top:110px;width:500px;height:320px;border-radius:20px;background:radial-gradient(ellipse at 60% 55%,#e6e0ea 0%,#eeeaf0 50%,var(--panel) 75%)}

/* benefits */
.benefits{left:0;top:1460px;width:1200px;height:597px;background:var(--white)}
.benefits h2{left:0;width:1200px;top:60px;text-align:center;color:var(--purple);font-size:28px}
.rule{left:540px;top:103px;width:120px;height:2px;background:#cfc3d6}
.carousel-arrow{top:258px}
.benefit{width:210px;text-align:center}
.benefit .hex{display:block;margin:0 auto}
.benefit h3{margin-top:30px;font-size:17px;font-weight:600;color:var(--ink)}
.benefit h3.hi{color:var(--purple)}
.benefit p{margin-top:18px;font-size:11px;line-height:18px;color:var(--grey-light)}

/* testimonials */
.testimonials{left:0;top:2057px;width:1200px;height:477px;background:radial-gradient(ellipse at 55% 60%,#6b4a78 0%,#4d3358 50%,#3a2742 100%)}
.testimonials h2{left:0;width:1200px;top:36px;text-align:center;color:var(--white);font-size:36px}
.quote{left:185px;top:118px;width:830px;text-align:center;color:var(--white);font-style:italic;font-size:15px;line-height:27px}
.avatar{left:553px;top:269px;width:94px;height:94px;border-radius:50%;background:linear-gradient(160deg,#e8c9a8,#b88c66);border:3px solid var(--white)}
.t-arrow{top:301px}
.t-name{left:0;width:1200px;top:383px;text-align:center;color:var(--white);font-weight:800;font-size:14px}

/* contact */
.contact{left:0;top:2534px;width:1200px;height:704px;background:var(--night)}
.contact h2{left:0;width:1200px;top:33px;text-align:center;color:var(--white);font-size:25px}
.contact .intro{left:330px;top:82px;width:540px;text-align:center;color:#9a9a9a;font-size:10px;line-height:14px}
.field{left:233px;width:732px;background:var(--field);border:1px solid var(--field-line);color:#6c6c6c;font-size:9.5px;letter-spacing:.5px;padding:16px 16px}
.submit{left:233px;top:596px;width:732px;height:51px;background:var(--purple);color:var(--white);font-weight:700;font-size:10px;letter-spacing:1px;display:flex;align-items:center;justify-content:center}
.note{left:233px;top:656px;width:732px;text-align:center;color:#4f4f4f;font-size:9px}

/* footer */
.footer{left:0;top:3238px;width:1200px;height:341px;background:var(--night-deep);color:var(--white)}
.footer .logo{left:70px;top:26px;font-size:40px}
.f-info{left:75px;top:112px;font-size:9px;line-height:14px;color:#bbbbbb}
.f-info div{display:flex;margin-bottom:13px}
.f-info b{width:75px;color:var(--white);font-weight:700}
.f-social{left:75px;top:218px;display:flex;gap:14px}
.f-social span{width:12px;height:12px;border-radius:50%;background:var(--white)}
.f-social span.first{background:var(--purple-soft)}
.f-sub h3,.f-links h3{font-size:20px;font-weight:700;font-family:"Fredoka","Open Sans",sans-serif}
.f-sub{left:407px;top:40px;width:360px}
.f-sub p{margin-top:10px;font-size:10px;line-height:14px;color:#555}
.f-input{margin-top:16px;width:353px;height:45px;background:#d8d8d8;color:#8a8a8a;font-size:10px;padding:15px 16px}
.f-btn{margin-top:16px;width:134px;height:45px;background:var(--magenta);font-size:10px;font-weight:700;display:flex;align-items:center;justify-content:center}
.f-links{left:877px;top:40px;width:280px}
.f-links ul{margin-top:22px;list-style:none;display:grid;grid-template-columns:108px 170px;row-gap:26px;font-size:10px;color:#cccccc}
.copyright{left:0;width:1200px;top:307px;text-align:center;font-size:9.5px;color:#555}
.copyright b{color:#888}
</style>
</head>
<body>

<header class="abs hero" role="img" aria-label="Dim photograph of a soft bed with rumpled sheets by a window">
  <div class="abs logo"><span class="mark"></span>Lullio</div>
  <nav class="abs main-nav">
    <span class="active">home</span><span>stream</span><span>instructions</span><span>what to expect</span><span>how to jump into sleep</span><span>other tricks for great sleep</span>
  </nav>
  <div class="abs slide-dots"><span class="on"></span><span></span><span></span><span></span><span></span></div>
  <div class="abs social"><span class="first"></span><span></span><span></span><span></span><span></span></div>
  <h1 class="abs hero-title">Sleep.Deep.Easy.</h1>
  <div class="abs btn-player">Go to player
    <svg width="18" height="20" viewBox="0 0 18 20"><path d="M2 1 L17 10 L2 19 Z" fill="#fff"/></svg>
  </div>
  <svg class="abs scroll-down" width="40" height="40" viewBox="0 0 40 40">
    <circle cx="20" cy="20" r="18" fill="none" stroke="#d0d0d0" stroke-width="2"/>
    <path d="M20 10 V28 M13 21 L20 28 L27 21" fill="none" stroke="#d0d0d0" stroke-width="3"/>
  </svg>
</header>

<section class="abs how">
  <h2 class="abs heading">HOW IT WORKS</h2>
  <p class="abs lead">In a recent study scientists observed laying in a bed that is rocking back and forth can literally make you sleep easier and deeper! For those who do not have a rocking bed (100% percent of the population). Lullio was created to answer these questions:</p>
  <ul class="abs">
    <li>What is it about repetitive back and forth movement that makes it so sedating?</li>
    <li>Is physically rocking the only way to capture the effect?</li>
    <li>Is it possible we don't necessarily need to be moving back and forth, we simply need to perceive back and forth movement?</li>
    <li>Can seeing or hearing repetitive back and forth movement have the same or similar effect?</li>
    <li>Isn't that how counting sheep works?</li>
  </ul>
  <p class="abs close">Lullio is white noise that oscillates in pitch to harness the calming and sedating effects of mundane repetition.</p>
  <div class="abs sheep-art" role="img" aria-label="Illustration of sheep jumping over a picket fence under a crescent moon"></div>
</section>

<section class="abs benefits">
  <h2 class="abs heading">PROVEN BENEFITS OF PLENTIFUL REST</h2>
  <div class="abs rule"></div>
  <svg class="abs carousel-arrow" style="left:76px" width="22" height="30" viewBox="0 0 22 30"><path d="M18 3 L6 15 L18 27" fill="none" stroke="#c4c4c4" stroke-width="5"/></svg>
  <svg class="abs carousel-arrow" style="left:1102px" width="22" height="30" viewBox="0 0 22 30"><path d="M4 3 L16 15 L4 27" fill="none" stroke="#c4c4c4" stroke-width="5"/></svg>

  <div class="abs benefit" style="left:162px;top:170px">
    <svg class="hex" width="170" height="190" viewBox="0 0 170 190" role="img" aria-label="Lightbulb icon"><polygon points="85,3 165,48 165,142 85,187 5,142 5,48" fill="#fff" stroke="#e6e6e6" stroke-width="5"/><polygon points="85,16 153,55 153,135 85,174 17,135 17,55" fill="#3a3a3a"/></svg>
    <h3>More energy</h3>
    <p>With Lullio playing in the background, we think you can expect to sleep a little bit easier and a little bit deeper.</p>
  </div>
  <div class="abs benefit" style="left:387px;top:170px">
    <svg class="hex" width="170" height="190" viewBox="0 0 170 190" role="img" aria-label="Lotus flower icon"><polygon points="85,3 165,48 165,142 85,187 5,142 5,48" fill="#fff" stroke="#e6e6e6" stroke-width="5"/><polygon points="85,16 153,55 153,135 85,174 17,135 17,55" fill="#a86bc6"/></svg>
    <h3 class="hi">A longer life</h3>
    <p>With Lullio playing in the background, we think you can expect to sleep a little bit easier and a little bit deeper.</p>
  </div>
  <div class="abs benefit" style="left:611px;top:170px">
    <svg class="hex" width="170" height="190" viewBox="0 0 170 190" role="img" aria-label="Smiling sheep icon"><polygon points="85,3 165,48 165,142 85,187 5,142 5,48" fill="#fff" stroke="#e6e6e6" stroke-width="5"/><polygon points="85,16 153,55 153,135 85,174 17,135 17,55" fill="#3a3a3a"/></svg>
    <h3>Better moods</h3>
    <p>With Lullio playing in the background, we think you can expect to sleep a little bit easier and a little bit deeper.</p>
  </div>
  <div class="abs benefit" style="left:840px;top:170px">
    <svg class="hex" width="170" height="190" viewBox="0 0 170 190" role="img" aria-label="Hands holding a heart icon"><polygon points="85,3 165,48 165,142 85,187 5,142 5,48" fill="#fff" stroke="#e6e6e6" stroke-width="5"/><polygon points="85,16 153,55 153,135 85,174 17,135 17,55" fill="#3a3a3a"/></svg>
    <h3>Fewer heart problems</h3>
    <p>With Lullio playing in the background, we think you can expect to sleep a little bit easier and a little bit deeper.</p>
  </div>
</section>

<section class="abs testimonials" role="img" aria-label="Purple-tinted photograph of a person resting in bed">
  <h2 class="abs heading">TESTIMONIALS</h2>
  <p class="abs quote">"Lorem ipsum dolor sit amet, consectetur adipiscing elit, sed do eiusmod tempor incididunt ut labore et dolore magna aliqua. Ut enim ad minim veniam, quis nostrud exercitation ullamco laboris nisi ut aliquip ex ea commodo consequat. Duis aute irure dolor in reprehenderit in voluptate velit esse cillum dolore eu fugiat nulla pariatur. Excepteur sint occaecat cupidatat non proident, sunt in culpa qui officia deserunt mollit anim id est laborum."</p>
  <svg class="abs t-arrow" style="left:508px" width="20" height="28" viewBox="0 0 20 28"><path d="M16 3 L5 14 L16 25" fill="none" stroke="#fff" stroke-width="5"/></svg>
  <div class="abs avatar" role="img" aria-label="Portrait photo of the reviewer"></div>
  <svg class="abs t-arrow" style="left:673px" width="20" height="28" viewBox="0 0 20 28"><path d="M4 3 L15 14 L4 25" fill="none" stroke="#fff" stroke-width="5"/></svg>
  <p class="abs t-name">DANA WHITFIELD // HIGH SCHOOL TEACHER</p>
</section>

<section class="abs contact">
  <h2 class="abs heading">HAVE QUESTIONS OR COMMENTS?</h2>
  <p class="abs intro">Lorem Ipsum is simply dummy text of the printing and typesetting industry. Lorem Ipsum has been the industry's standard dummy text ever since the 1500s, when an unknown printer took a galley of type and scrambled it to make a type specimen book.</p>
  <div class="abs field" style="top:158px;height:52px">YOUR FULL NAME *</div>
  <div class="abs field" style="top:238px;height:52px">YOUR E-MAIL ADDRESS *</div>
  <div class="abs field" style="top:313px;height:52px">YOUR PHONE NUMBER</div>
  <div class="abs field" style="top:389px;height:179px">YOUR MESSAGE *</div>
  <div class="abs submit">SUBMIT</div>
  <p class="abs note">* We never share your details. Fields marked with an asterisk are required so we can reply to your note quickly.</p>
</section>

<footer class="abs footer">
  <div class="abs logo"><span class="mark"></span>Lullio</div>
  <div class="abs f-info">
    <div><b>Street Adress:</b><span>14 Linden Row, Marlowbay CA<br>90210</span></div>
    <div><b>Email us at:</b><span>help@lullio.com</span></div>
    <div><b>Call us at:</b><span>(555) 014 7730</span></div>
  </div>
  <div class="abs f-social"><span class="first"></span><span></span><span></span><span></span><span></span></div>
  <div class="abs f-sub">
    <h3>SUBSCRIBE TO OUR MAILING LIST</h3>
    <p>Don't worry we won't spam. We will only provide informations and news about our product.</p>
    <div class="f-input">email address</div>
    <div class="f-btn">SUBSCRIBE</div>
  </div>
  <div class="abs f-links">
    <h3>QUICK LINKS</h3>
    <ul>
      <li>home</li><li>how to jump into sleep</li>
      <li>stream</li><li>other tips for great sleep</li>
      <li>instructions</li><li>contact us</li>
      <li>what to expect</li><li></li>
    </ul>
  </div>
  <p class="abs copyright">Copyright © 2017 <b>LULLIO</b>. Use of this website constitutes acceptance of our <b>User Agreement</b> and <b>Privacy Policy</b>.</p>
</footer>

</body>
</html>
```